Cover Design Brief – Prayer Book (Modern Revision)

Design a new, modern, high-quality book cover that reflects the essence of the original version. The updated cover should feel contemporary yet familiar, appealing to both younger and older readers, while evoking a sense of spiritual depth, calm, and authenticity.

1. Visual Reference to the Original Cover
Continuity:
Retain visual elements such as the color palette, central motifs (eg, geometric patterns, Islamic ornaments, or a symbolic figure), and overall structure from the original cover.

Recognition:
Readers familiar with the old cover should instantly recognize the book but be pleasantly surprised by the refined, modern look.

2. Style & Mood
Modern Islamic design, minimalist and clean rather than ornate.

Spiritual, calming, elegant – avoid overly bright or flashy visuals.

Subtle use of Islamic motifs, possibly a decorative Arabic calligraphy word like ṣalāh (صلاة) to enrich the theme.

3. Suggested Color Palette
Deep blue, teal, petrol green, olive, sand tones, or midnight blue with accents of gold – depending on the original cover scheme.

Avoid neon or loud colors.

If gold or silver is used, it should be subtle and classy (eg, foil stamping or embossing, not digital effects).

4. Typography
A modern serif font for the main title is welcome, but it should be clean and elegant.

Subtitles should use a clear, legible font.

If the title includes Arabic text, it should be displayed in tasteful classical calligraphy or a stylized script.

5. Back Cover
Will include a brief description text (to be provided later).

Clean layout, optionally with a small publisher logo.

Possibly a short quote or ḥadīth in Arabic (with or without translation) to complement the design.

6. Target Audience
German-speaking Muslims, male and female, ages 15+

Suitable for both beginners and advanced practitioners of the prayer

Designed as a long-term spiritual companion and a thoughtful gift

```html
<!DOCTYPE html>
<html lang="de">
<head>
<meta charset="utf-8">
<title>Aṣ-Ṣalāh – Das Gebet im Islam</title>
<link rel="stylesheet" href="https://fonts.googleapis.com/css2?family=Noto+Serif:wght@400;500&display=swap">
<style>
  :root {
    --paper: #ffffff;
    --sun: #f2b93f;
    --sand: #f7cf6e;
    --coral: #ef6f50;
    --navy: #1e2e47;
    --teal: #2f8686;
    --ink-light: #fff8ec;
    --panel: rgba(88, 84, 80, 0.86);
    --serif: "Noto Serif", Georgia, serif;
  }
  * { box-sizing: border-box; margin: 0; padding: 0; }
  html, body { width: 900px; height: 1200px; overflow: hidden; background: var(--paper); }
  body { position: relative; font-family: var(--serif); }

  .front-cover {
    position: absolute;
    overflow: hidden;
    color: var(--ink-light);
  }
  .front-cover--single {
    left: 232px; top: 40px; width: 425px; height: 607px;
    font-size: 10px;
    box-shadow: -14px 14px 28px rgba(0,0,0,.28);
  }
  .front-cover--wrap {
    left: 460px; top: 707px; width: 316px; height: 454px;
    font-size: 7.44px;
  }

  .cover-illustration {
    position: absolute; inset: 0;
    background: linear-gradient(180deg, var(--sun) 0%, var(--sand) 38%, var(--coral) 62%, var(--teal) 72%, var(--navy) 100%);
  }
  .salah-emblem {
    position: absolute; left: 42.3%; top: 5.8%;
    width: 11.5%; aspect-ratio: 1; border-radius: 50%;
    border: 0.2em solid var(--ink-light);
    background: rgba(255,248,236,.18);
  }
  .cover-title, .cover-subtitle, .cover-subtitle-line2, .edition-note {
    position: absolute; font-weight: 500; line-height: 1; white-space: nowrap;
    text-shadow: 0 0 .3em rgba(120,70,0,.35);
  }
  .cover-title { left: 0; right: 0; top: 15.6%; text-align: center; font-size: 6.4em; }
  .cover-subtitle { left: 0; right: 0; top: 28%; text-align: center; font-size: 3.8em; }
  .cover-subtitle-line2 { right: 16.5%; top: 34.3%; font-size: 3em; }
  .edition-note { left: 0; right: 0; text-align: center; font-size: 1.8em; font-weight: 400; }
  .edition-note--first { top: 43.4%; }
  .edition-note--second { top: 47.8%; }

  .publisher-mark {
    position: absolute; left: 11.5%; top: 88%;
    width: 11.5%; aspect-ratio: 1; background: var(--teal);
  }
  .publisher-name {
    position: absolute; left: 56%; top: 92.8%;
    font-size: 1.5em; line-height: 1; white-space: nowrap;
  }

  .spine {
    position: absolute; left: 429px; top: 707px; width: 31px; height: 454px;
    background: var(--navy); color: var(--ink-light);
  }
  .spine-title {
    position: absolute; left: 50%; top: 220px;
    transform: translate(-50%, -50%) rotate(-90deg);
    white-space: nowrap; font-size: 15px; font-weight: 500;
  }
  .spine-mark { position: absolute; left: 9px; top: 400px; width: 13px; height: 13px; background: var(--teal); }

  .back-cover {
    position: absolute; left: 113px; top: 707px; width: 316px; height: 454px;
    overflow: hidden; color: var(--ink-light);
  }
  .back-illustration {
    position: absolute; inset: 0;
    background: linear-gradient(180deg, var(--sand) 0%, var(--sun) 40%, #e8a45a 70%, var(--coral) 100%);
  }
  .back-title { position: absolute; left: 101px; top: 65px; font-size: 16px; font-weight: 500; }
  .back-emblem {
    position: absolute; left: 193px; top: 56px; width: 34px; height: 34px;
    border-radius: 50%; border: 1.5px solid var(--ink-light); background: rgba(255,248,236,.18);
  }
  .blurb-panel { position: absolute; left: 49px; top: 96px; width: 221px; height: 279px; background: var(--panel); }
  .back-publisher {
    position: absolute; left: 40px; top: 392px;
    display: flex; align-items: center; gap: 5px; font-size: 8px;
  }
  .back-publisher__square { width: 18px; height: 18px; background: var(--teal); }
</style>
</head>
<body>

<section class="front-cover front-cover--single">
  <div class="cover-illustration" role="img" aria-label="Flat illustration of a mosque with domes and two minarets against a golden sky and teal hills"></div>
  <div class="salah-emblem" role="img" aria-label="Arabic calligraphy of the word ṣalāh in a circle"></div>
  <h1 class="cover-title">Aṣ-Ṣalāh</h1>
  <p class="cover-subtitle">Das Gebet</p>
  <p class="cover-subtitle-line2">im Islam</p>
  <p class="edition-note edition-note--first">Vollstadig</p>
  <p class="edition-note edition-note--second">revidierte Ausgabe</p>
  <span class="publisher-mark"></span>
  <p class="publisher-name">Verlag Lichtweg</p>
</section>

<section class="back-cover">
  <div class="back-illustration" role="img" aria-label="Flat illustration of an old town skyline in warm sand and coral tones"></div>
  <p class="back-title">Aṣ-Ṣalāh</p>
  <div class="back-emblem" role="img" aria-label="Arabic calligraphy of the word ṣalāh in a circle"></div>
  <div class="blurb-panel"></div>
  <div class="back-publisher"><span class="back-publisher__square"></span><span>Verlag Lichtweg</span></div>
</section>

<section class="spine">
  <p class="spine-title">Aṣ-Ṣalāh - Das Gebet im Islam</p>
  <span class="spine-mark"></span>
</section>

<section class="front-cover front-cover--wrap">
  <div class="cover-illustration" role="img" aria-label="Flat illustration of a mosque with domes and two minarets against a golden sky and teal hills"></div>
  <div class="salah-emblem" role="img" aria-label="Arabic calligraphy of the word ṣalāh in a circle"></div>
  <h1 class="cover-title">Aṣ-Ṣalāh</h1>
  <p class="cover-subtitle">Das Gebet</p>
  <p class="cover-subtitle-line2">im Islam</p>
  <p class="edition-note edition-note--first">Vollstadig</p>
  <p class="edition-note edition-note--second">revidierte Ausgabe</p>
  <span class="publisher-mark"></span>
  <p class="publisher-name">Verlag Lichtweg</p>
</section>

</body>
</html>
```